Website Redesign for Mortgage, Property and Conveyancing business

Project Overview:
We are looking for a refresh and redesign of our current website to a smart, crisp and fresh approach to Home Loans, Conveyancing and Property sales. This task will be to:
- Redesign our current website in accordance with the new wireframe.
- Provide all elements required for the design
- Build 7 key templates including:
Home Page
2nd Level Section Page
3rd level Product landing Page
2nd Level - About Us, Contact Us etc
Blog
Blog Article
Campaign Page - no header
Technical
The design is for a Wordpress website. Existing theme is Quillnest and we use Elementor for page editing. We are open to a new theme to be introduced but would prefer to stay with elementor.
Current Site is: www.corvanta.com.au
Sites that we like or elements of sites:
Pelham Real Estate: https://www.pelham-example.com.au/ (Like use of video and navigation)
Copper Lantern Lane - Mortage: https://cll-example.com.au/refinance-home-loan/ (Like landing pages a sin example)
Marquetry: https://marquetry-example.com.au/ (like Our services section).
Industry/Entity Type
Mortgage, Property, Conveyancing, Property Investment
Coding
Coded - Design and coding required
Number of Pages Required
5+ page
Font styles to use
Requirements
Must have
- Built for Wordpress and Elementor.
Nice to have
- See Project Description for links to ideas/elements that we have liked. However, open to ideas as long as the follow the navigation set out in the wire frame.

```html
<!DOCTYPE html>
<html lang="en">
<head>
<meta charset="utf-8">
<title>Corvanta Group Services</title>
<link rel="stylesheet" href="https://fonts.googleapis.com/css2?family=Fira+Sans:wght@400;500&family=Roboto:wght@400;500;700&display=swap">
<style>
:root{
  --blue:#1b5fae;
  --navy:#0c4a8c;
  --mid:#1f72c6;
  --green:#86b83a;
  --ink:#222;
  --muted:#666;
  --soft:#eef4fb;
  --grey:#f2f2f2;
}
*{margin:0;padding:0;box-sizing:border-box}
html,body{width:1200px;height:4804px;overflow:hidden}
body{font-family:Roboto,Arial,sans-serif;color:var(--ink);background:#fff;position:relative}
.abs{position:absolute}
h2{font-family:"Fira Sans",Roboto,sans-serif;font-weight:400;font-size:38px;text-align:center;color:#1d1d1d;position:absolute;left:0;width:1200px}

.site-header{top:0;left:0;width:1200px;height:72px;background:#fff;border-bottom:1px solid #ddd}
.brand{left:110px;top:14px;display:flex;align-items:center;gap:10px}
.brand-mark{width:44px;height:44px;background:var(--blue)}
.brand-name{font-size:32px;font-weight:500;color:var(--navy);line-height:1}
.menu-btn{right:110px;top:20px;width:42px}
.menu-btn span{display:block;height:4px;background:#222;margin-bottom:9px;border-radius:2px}

.hero{top:72px;left:0;width:1200px;height:654px;background:linear-gradient(100deg,#3a4552 0%,#6d7985 40%,#c9ccd0 70%,#e9e6e1 100%)}
.hero h1{left:103px;top:232px;font-family:"Fira Sans",Roboto,sans-serif;font-weight:500;font-size:64px;line-height:70px;color:#fff;text-shadow:0 2px 6px rgba(0,0,0,.45)}
.hero p{left:103px;top:396px;font-size:26px;color:#fff;text-shadow:0 1px 4px rgba(0,0,0,.5)}
.btn-start{left:104px;top:462px;width:150px;height:46px;background:var(--blue);color:#fff;font-weight:700;font-size:15px;display:flex;align-items:center;justify-content:center;gap:10px;border-radius:4px}
.play{left:799px;top:273px}

.services{top:726px;left:0;width:1200px;height:437px;background:var(--soft)}
.service-card{width:278px;height:194px;top:157px;background:#fff;border-radius:10px;text-align:center;padding-top:22px;box-shadow:0 4px 14px rgba(0,0,0,.05)}
.service-card h3{font-size:15px;font-weight:500;margin-top:14px}
.service-card p{font-size:14px;color:#444;line-height:25px;margin-top:4px}
.icon-ring{width:76px;height:76px;border-radius:50%;margin:0 auto;border:4px solid #d8ebc3;background:var(--green);display:flex;align-items:center;justify-content:center}

.why{top:1163px;left:0;width:1200px;height:574px;background:#fff}
.why-card{top:167px;width:235px;height:310px;background:#f1f1f1;text-align:center;padding:40px 10px 0}
.why-card.active{background:#fff;box-shadow:0 6px 24px rgba(0,0,0,.12);border-bottom:4px solid var(--green)}
.why-card h3{font-size:16px;font-weight:700;margin-top:22px;line-height:20px}
.why-card p{font-size:12.5px;color:var(--muted);line-height:22px;margin-top:10px}
.why-icon{width:88px;height:88px;border-radius:50%;margin:0 auto;background:var(--navy);display:flex;align-items:center;justify-content:center}
.why-icon.green{background:var(--green)}

.subscribe{top:1737px;left:0;width:1200px;height:332px;background:linear-gradient(90deg,#124e99,#1a62b6 50%,#124e99)}
.subscribe h2{color:#fff;top:76px;line-height:46px;font-size:38px}
.field{top:204px;height:46px;background:#fff;font-size:15px;color:#333;padding:14px 20px}
.sub-btn{top:204px;left:886px;width:165px;height:46px;background:var(--green);color:#fff;font-weight:700;font-size:14px;display:flex;align-items:center;justify-content:center}

.team{top:2069px;left:0;width:1200px;height:521px}
.member{top:161px;width:231px;height:274px;background:#fff;box-shadow:0 2px 8px rgba(0,0,0,.15);text-align:center;overflow:hidden}
.member .photo{height:216px;background:linear-gradient(180deg,#d6d3d3,#c3c0c1)}
.member .slash{position:absolute;left:0;top:186px;width:231px;height:40px}
.member h4{font-size:14px;font-weight:700;margin-top:14px}
.member p{font-size:13px;color:#555;margin-top:4px}

.blog{top:2590px;left:0;width:1200px;height:485px;background:var(--grey)}
.post{top:75px;width:273px}
.post .img{height:263px}
.post p{text-align:center;font-size:15px;color:#333;line-height:24px;margin-top:22px}

.reviews{top:3075px;left:0;width:1200px;height:454px}
.avatar{width:75px;height:75px;border-radius:50%;background:linear-gradient(180deg,#cfcfcf,#9aa3ad)}
.quote{font-family:"Fira Sans",sans-serif;font-size:64px;color:var(--green);line-height:1}
.stars{font-size:16px;color:var(--green);letter-spacing:2px}
.review-text{width:320px;font-size:15px;color:#555;line-height:26px;text-align:justify}
.divider{left:599px;top:181px;width:1px;height:187px;background:#ccc}

.lenders{top:3529px;left:0;width:1200px;height:448px;background:linear-gradient(90deg,#7fb236,#8cbf3f 50%,#7fb236)}
.lenders h2{color:#fff;top:222px;font-size:46px;font-weight:500}

.family{top:3977px;left:0;width:1200px;height:765px;background:linear-gradient(120deg,#e8e6e3,#d9cfc4 45%,#b99d86 70%,#ece9e5)}
.info{top:515px;width:321px;height:250px;color:#fff;padding:34px 0 0 68px;background:var(--navy)}
.info.mid{background:var(--mid)}
.info h3{font-size:20px;font-weight:500;margin-top:20px}
.info p{font-size:15px;line-height:24px;margin-top:14px}
.info p+p{margin-top:10px}
.socials{display:flex;gap:10px;margin-top:6px}
.socials span{width:30px;height:30px;border-radius:50%;background:#fff}

.site-footer{top:4742px;left:0;width:1200px;height:62px;background:var(--green);color:#fff;font-size:14px;text-align:center;line-height:62px}
</style>
</head>
<body>

<header class="site-header abs">
  <div class="brand abs"><span class="brand-mark"></span><span class="brand-name">Corvanta</span></div>
  <div class="menu-btn abs"><span></span><span></span><span></span></div>
</header>

<section class="hero abs" role="img" aria-label="Hand passing house keys above a small model house">
  <h1 class="abs">Finance, Property,<br>Conveyancing</h1>
  <p class="abs">Unlocking Opportunities and solving problems</p>
  <div class="btn-start abs">GET STARTED
    <svg width="14" height="14" viewBox="0 0 14 14"><circle cx="7" cy="7" r="7" fill="#fff"/><path d="M5.5 4l3 3-3 3" stroke="#1b5fae" stroke-width="2" fill="none"/></svg>
  </div>
  <svg class="play abs" width="112" height="112" viewBox="0 0 112 112">
    <circle cx="56" cy="56" r="54" fill="#dfe6f2"/>
    <circle cx="56" cy="56" r="42" fill="#1b4d94"/>
    <circle cx="56" cy="56" r="24" fill="#fff"/>
    <path d="M50 45l17 11-17 11z" fill="#1b4d94"/>
  </svg>
</section>

<section class="services abs">
  <h2 style="top:74px">Our Services</h2>
  <div class="service-card abs" style="left:144px">
    <div class="icon-ring"><svg width="36" height="36" viewBox="0 0 36 36" fill="none" stroke="#fff" stroke-width="2.5"><rect x="6" y="10" width="24" height="16" rx="2"/><path d="M6 16h24"/></svg></div>
    <h3>FINANCE</h3><p>Finance For Your Home, Car,<br>Investments, And Assets</p>
  </div>
  <div class="service-card abs" style="left:461px">
    <div class="icon-ring"><svg width="36" height="36" viewBox="0 0 36 36" fill="none" stroke="#fff" stroke-width="2.5"><path d="M5 18L18 7l13 11M9 15v14h18V15"/></svg></div>
    <h3>PROPERTY</h3><p>Property Sales, Purchases, And<br>Rentals</p>
  </div>
  <div class="service-card abs" style="left:778px">
    <div class="icon-ring"><svg width="36" height="36" viewBox="0 0 36 36" fill="none" stroke="#fff" stroke-width="2.5"><path d="M8 30V14l10-8 10 8v16zM18 26V14M13 19l5-5 5 5"/></svg></div>
    <h3>CONVEYANCING</h3><p>Conveyancing For Seamless<br>Property Transactions</p>
  </div>
</section>

<section class="why abs">
  <h2 style="top:70px">Why Corvanta</h2>
  <div class="why-card abs" style="left:93px">
    <div class="why-icon"><svg width="48" height="48" viewBox="0 0 48 48" fill="none" stroke="#fff" stroke-width="2.5"><circle cx="24" cy="18" r="5"/><circle cx="12" cy="24" r="4"/><circle cx="36" cy="24" r="4"/><path d="M16 38c0-6 4-10 8-10s8 4 8 10M6 38c0-4 3-7 6-7M42 38c0-4-3-7-6-7"/></svg></div>
    <h3>20 years Experience</h3>
    <p>We have grown and changed with the industry, and we're dedicated to continually improve our service and products so you get the best solutions possible.</p>
  </div>
  <div class="why-card active abs" style="left:353px">
    <div class="why-icon green"><svg width="44" height="44" viewBox="0 0 44 44" fill="none" stroke="#fff" stroke-width="2.5"><rect x="10" y="6" width="24" height="32" rx="2"/><path d="M15 14h14M15 21h14M15 28h8"/></svg></div>
    <h3>We give you choice</h3>
    <p>We have grown and changed with the industry, and we're dedicated to continually improve our service and products so you get the best solutions possible.</p>
  </div>
  <div class="why-card abs" style="left:612px">
    <div class="why-icon"><svg width="50" height="44" viewBox="0 0 50 44" fill="none" stroke="#fff" stroke-width="2.5"><circle cx="15" cy="14" r="6"/><circle cx="35" cy="14" r="6"/><path d="M3 38c0-8 5-13 12-13s12 5 12 13M23 38c0-8 5-13 12-13s12 5 12 13"/></svg></div>
    <h3>It is about the outcome</h3>
    <p>When we say we care, we mean it. If you are a client now, we want you to be a happy client. If we cannot help you become a client today we'd like to help you tomorrow.</p>
  </div>
  <div class="why-card abs" style="left:870px;padding-top:22px">
    <div class="why-icon"><svg width="46" height="46" viewBox="0 0 46 46" fill="none" stroke="#fff" stroke-width="2.5"><path d="M8 20L23 8l15 12M12 17v17h22V17"/><circle cx="23" cy="25" r="5"/></svg></div>
    <h3>We give you options that makes sense</h3>
    <p>Our team of finance, property investment and accounting experts know what they are talking about, and they are happy to take the time to explain things clearly.</p>
  </div>
</section>

<section class="subscribe abs">
  <h2>Subscribe To Keep Up To Date<br>On Market News</h2>
  <div class="field abs" style="left:149px;width:351px">Enter Name</div>
  <div class="field abs" style="left:519px;width:351px">Enter Email</div>
  <div class="sub-btn abs">SUBSCRIBE NOW</div>
</section>

<section class="team abs">
  <h2 style="top:80px">Our Team</h2>
  <div class="member abs" style="left:110px"><div class="photo" role="img" aria-label="Portrait of team member"></div><svg class="slash" viewBox="0 0 231 40" preserveAspectRatio="none"><path d="M0 40L231 0v10L0 40z" fill="#1b4d94"/><path d="M0 40L231 10v30z" fill="#fff"/></svg><h4>Jhon Deo</h4><p>Lorem ipsum dolor sit amet</p></div>
  <div class="member abs" style="left:358px"><div class="photo" role="img" aria-label="Portrait of team member"></div><svg class="slash" viewBox="0 0 231 40" preserveAspectRatio="none"><path d="M0 40L231 0v10L0 40z" fill="#1b4d94"/><path d="M0 40L231 10v30z" fill="#fff"/></svg><h4>Jhon Deo</h4><p>Lorem ipsum dolor sit amet</p></div>
  <div class="member abs" style="left:608px"><div class="photo" role="img" aria-label="Portrait of team member"></div><svg class="slash" viewBox="0 0 231 40" preserveAspectRatio="none"><path d="M0 40L231 0v10L0 40z" fill="#1b4d94"/><path d="M0 40L231 10v30z" fill="#fff"/></svg><h4>Jhon Deo</h4><p>Lorem ipsum dolor sit amet</p></div>
  <div class="member abs" style="left:857px"><div class="photo" role="img" aria-label="Portrait of team member"></div><svg class="slash" viewBox="0 0 231 40" preserveAspectRatio="none"><path d="M0 40L231 0v10L0 40z" fill="#1b4d94"/><path d="M0 40L231 10v30z" fill="#fff"/></svg><h4>Jhon Deo</h4><p>Lorem ipsum dolor sit amet</p></div>
</section>

<section class="blog abs">
  <article class="post abs" style="left:140px"><div class="img" role="img" aria-label="Woman shrugging in a yellow sweater, article cover" style="background:linear-gradient(180deg,#f3b51b,#e2a219)"></div><p>Credit Scores – What Are They And<br>And How Do They Affect You</p></article>
  <article class="post abs" style="left:463px"><div class="img" role="img" aria-label="Credit rating form with calculator, article cover" style="background:linear-gradient(150deg,#d7262f,#e9e4de 55%,#b7c45a)"></div><p>Credit Scores – What Are They And<br>And How Do They Affect You</p></article>
  <article class="post abs" style="left:787px"><div class="img" role="img" aria-label="Woman holding a tablet in front of a house, article cover" style="background:linear-gradient(180deg,#c9ced4,#6f88a8 60%,#2f4f7f)"></div><p>Credit Scores – What Are They And<br>And How Do They Affect You</p></article>
</section>

<section class="reviews abs">
  <h2 style="top:86px">Read what our clients say About us</h2>
  <div class="avatar abs" role="img" aria-label="Client portrait" style="left:112px;top:189px"></div>
  <div class="quote abs" style="left:211px;top:196px">&#8220;</div>
  <div class="stars abs" style="left:211px;top:222px">★★★★★</div>
  <p class="review-text abs" style="left:211px;top:250px">Lorem ipsum dolor site ameted consectetur adipiscing sed do eiusmod tempor incididunt ut labore et dolore magna aliquat Uted enim ad minim veniam, quis nostrud exercitation.</p>
  <div class="divider abs"></div>
  <div class="avatar abs" role="img" aria-label="Client portrait" style="left:670px;top:189px"></div>
  <div class="quote abs" style="left:771px;top:196px">&#8220;</div>
  <div class="stars abs" style="left:771px;top:222px">★★★★★</div>
  <p class="review-text abs" style="left:771px;top:250px">Lorem ipsum dolor site ameted consectetur adipiscing sed do eiusmod tempor incididunt ut labore et dolore magna aliquat Uted enim ad minim veniam, quis nostrud exercitation.</p>
</section>

<section class="lenders abs" role="img" aria-label="Green-tinted handshake background">
  <h2>Our Panel of Lenders Large and small</h2>
</section>

<section class="family abs" role="img" aria-label="Smiling mother and daughter playing at home">
  <div class="info abs" style="left:106px">
    <svg width="70" height="60" viewBox="0 0 70 60" fill="none" stroke="#fff" stroke-width="2.5"><circle cx="38" cy="32" r="22"/><path d="M38 18v14l9 6M30 6h16M2 26h12M4 34h10M6 42h10"/></svg>
    <h3>Opening Times</h3>
    <p>Monday – Friday: 9am-5pm</p>
    <p>Saturday – Sunday: Closed</p>
  </div>
  <div class="info mid abs" style="left:437px">
    <svg width="70" height="60" viewBox="0 0 70 60" fill="none" stroke="#fff" stroke-width="2.5"><path d="M10 10c-4 4-4 12 8 26s24 18 28 12l4-6-9-7-5 4c-4-2-10-8-13-13l4-5-7-9z"/><circle cx="50" cy="18" r="12"/></svg>
    <h3>Contact Us</h3>
    <p>info@corvanta.com.au</p>
    <p>1300 555 017</p>
  </div>
  <div class="info abs" style="left:767px">
    <svg width="70" height="60" viewBox="0 0 70 60" fill="none" stroke="#fff" stroke-width="2.5"><path d="M24 58S6 36 6 22a18 18 0 0 1 36 0c0 14-18 36-18 36z"/><circle cx="24" cy="22" r="6"/></svg>
    <h3>Reach Us</h3>
    <p>22 Fernvale Drive, Ashcombe,<br>VIC 3170</p>
    <div class="socials"><span></span><span></span></div>
  </div>
</section>

<footer class="site-footer abs">2024 Copyright · Corvanta &nbsp;| All Rights Reserved</footer>

</body>
</html>
```